Bright Fern Billboard

We need to build a billboard that promotes our dispensary and showcases our Monday thru Thursday deal of 18% off the entire store for Happy Hour. I have attached the logo we want to use. We dont want to use the same colors from the logo as the main colors of the billboard. We need to add both locations to the artwork "5th and Harlow / Corwin and Tilbury". This board needs to POP and have a WOW factor to catch peoples attention. Here are the details outlined:
-Need Bright Fern logo attached to this on the billboard front and center
-Happy Hour - 18% off ENTIRE STORE from 2p-4:20p -Mon -Thurs
-Locations: 5th and Harlow / Corwin and West of Tilbury

```html
<!DOCTYPE html>
<html lang="en">
<head>
<meta charset="utf-8">
<title>Bright Fern Billboard</title>
<link rel="stylesheet" href="https://fonts.googleapis.com/css2?family=Anton&family=Archivo+Black&family=Montserrat:wght@700&family=Oswald:wght@500&display=swap">
<style>
  :root {
    --stage: #262626;
    --navy: #1b3d70;
    --yellow: #f7d630;
    --orange: #f07a2e;
    --orange-deep: #c8321c;
    --ink: #1c1c1c;
    --red: #c8142a;
    --coral: #ee7270;
    --band: #e3e3e3;
    --white: #ffffff;
    --shadow-gold: #b89a14;
  }
  html, body {
    margin: 0;
    width: 1170px;
    height: 1200px;
    overflow: hidden;
    background: var(--stage);
  }
  .billboard {
    position: absolute;
    left: 30px;
    top: 484px;
    width: 1110px;
    height: 232px;
    display: block;
    box-shadow: 0 4px 14px rgba(0,0,0,.45);
  }
  .brand-name { font-family: "Montserrat", sans-serif; font-weight: 700; fill: var(--navy); }
  .brand-tagline { font-family: "Montserrat", sans-serif; font-weight: 700; fill: var(--navy); letter-spacing: 5px; }
  .locations { font-family: "Oswald", sans-serif; font-weight: 500; fill: #222; }
  .locations .highlight { fill: var(--red); }
  .happy-hour { font-family: "Anton", sans-serif; fill: var(--white); }
  .discount { font-family: "Anton", sans-serif; fill: var(--navy); }
  .discount-shadow { font-family: "Anton", sans-serif; fill: var(--shadow-gold); }
  .entire-store { font-family: "Archivo Black", sans-serif; fill: var(--white); letter-spacing: 9px; }
  .schedule { font-family: "Archivo Black", sans-serif; fill: var(--ink); letter-spacing: 1px; }
</style>
</head>
<body>
<svg class="billboard" viewBox="0 0 1705 356" xmlns="http://www.w3.org/2000/svg" role="img" aria-label="Bright Fern Happy Hour billboard">
  <defs>
    <linearGradient id="paperFade" x1="0" y1="0" x2="1" y2="1">
      <stop offset="0" stop-color="#ffffff"/>
      <stop offset="1" stop-color="#f0f0f0"/>
    </linearGradient>
    <linearGradient id="orangeFade" x1="0" y1="0" x2="1" y2="0">
      <stop offset="0" stop-color="var(--orange)"/>
      <stop offset="0.55" stop-color="var(--orange)"/>
      <stop offset="1" stop-color="var(--orange-deep)"/>
    </linearGradient>
  </defs>

  <!-- brand side -->
  <rect class="brand-panel" x="0" y="0" width="1705" height="356" fill="url(#paperFade)"/>
  <rect class="location-band" x="0" y="278" width="1100" height="78" fill="var(--band)"/>

  <circle class="brand-dot" cx="160" cy="150" r="78" fill="var(--coral)"/>
  <text class="brand-name" x="305" y="185" font-size="128" textLength="700" lengthAdjust="spacingAndGlyphs">Bright Fern</text>
  <text class="brand-tagline" x="310" y="245" font-size="33">CANNABIS DISPENSARY</text>

  <g class="location-pin" transform="translate(107 318)">
    <path d="M0 -20 a15 15 0 0 1 15 15 c0 11 -15 26 -15 26 s-15 -15 -15 -26 a15 15 0 0 1 15 -15z" fill="var(--navy)"/>
    <circle cx="0" cy="-5" r="6" fill="var(--white)"/>
  </g>
  <text class="locations" x="140" y="335" font-size="36">5TH AND HARLOW / CORWIN AND <tspan class="highlight">WEST OF TILBURY</tspan></text>

  <!-- offer side -->
  <polygon class="navy-wedge" points="1045,0 1225,0 1152,172" fill="var(--navy)"/>
  <line class="accent-line" x1="1038" y1="0" x2="1112" y2="115" stroke="var(--yellow)" stroke-width="5"/>
  <polygon class="offer-panel" points="1232,0 1705,0 1705,356 1070,356" fill="var(--yellow)"/>
  <line class="edge-line" x1="1140" y1="188" x2="1052" y2="356" stroke="var(--ink)" stroke-width="4"/>

  <path class="happy-hour-band" d="M1185 32 L1705 0 L1705 74 L1185 118 a43 43 0 0 1 0 -86z" fill="url(#orangeFade)"/>
  <g class="clock-icon" transform="translate(1192 78)" fill="none" stroke="var(--white)" stroke-width="6" stroke-linecap="round">
    <circle r="22"/>
    <path d="M0 -11 V0 L8 6"/>
    <path d="M-18 -24 l-8 8 M18 -24 l8 8"/>
  </g>
  <text class="happy-hour" transform="translate(1245 100) rotate(-5)" font-size="62" textLength="410" lengthAdjust="spacingAndGlyphs">HAPPY HOUR</text>

  <line class="rule" x1="1455" y1="109" x2="1705" y2="86" stroke="var(--ink)" stroke-width="5"/>

  <text class="discount-shadow" transform="translate(1216 233) rotate(-5) skewX(-8)" font-size="90" textLength="440" lengthAdjust="spacingAndGlyphs">18% OFF</text>
  <text class="discount" transform="translate(1210 228) rotate(-5) skewX(-8)" font-size="90" textLength="440" lengthAdjust="spacingAndGlyphs">18% OFF</text>

  <polygon class="store-band" points="1112,252 1705,202 1705,270 1082,322" fill="var(--ink)"/>
  <text class="entire-store" transform="translate(1145 304) rotate(-5)" font-size="46" textLength="520">ENTIRE STORE</text>

  <text class="schedule" transform="translate(1152 348) rotate(-4)" font-size="26" textLength="470">FROM 2P-4:20P -MON -THURS</text>
</svg>
</body>
</html>
```